Voidcraft Q Fundlaunch Graphic Design

My name is Tom, I design 3d-printable spaceships in 28mm scale. I have had four successful Fundlaunches, and for my fifth one, I want to take the graphic design of the campaign to the next level.
(see my last one here for an idea of what I am looking for, but better than the shitty graphics I myself made the last four times around: https://www.fundlaunch-example.com/projects/7thcrownworks/voidcraft-iii-basilisk-modular-3d-printable-28mm-spaceship )

I am looking for a new sci-fi themed graphic design profile for the Fundlaunch page. This will include:
- Header design (I use images rather than fonts for titles) template in psd format that can have its text and colour changed easily by a third party, with a suitable sci-fi font.
- A sci-fi frames design for presenting 3D renders (with alpha channels) of miniatures, add-ons, stretch goals, framing photographic images, and presenting information, such as a chart of various campaign pledges
- Icons for locked and unlocked to be used in the frame above to show whether a stretch goal has been reached or is still being worked towards

I am looking for the creation of a series of photoshop templates that myself and my colleague can use to fill in the information needed for the campaign.

Thematically, the ship is designed with the same design language as the Halvorsen from the Drift universe (see https://driftverse.wikiplace-example.org/wiki/The_Drift_(TV) for a little more information and existing design profiles for the TV series, books and RPG), and I am looking to have a similar feel to this in my own graphic profile, without it being an outright copy. Something befitting a hard sci-fi universe.

The graphic profile must work well within the bounds of Fundlaunch's limitations and graphic profile. Graphics must be 680 pixels wide, and fit with the stark white background of Fundlaunch. We have no control over spacing between images (imagine it is a word press with sections), so there will be white space between them and any text, and or the next image, something to keep in mind.

Professional quality graphics, the use of colour to both categorise sections of the page (stretch goals, ship details, add-ons, pledges, etc) and lift otherwise mainly monotone renders, also would help work against the tedium of Fundlaunch's graphic profile.

The new ship looks like this:
https://www.filecrate-example.com/s/8zk2pwnrt5ybq3m/Final%20Form%20Front%20PDCs.png?dl=0

And you can see more images of WIP on my instagram below.
https://www.snapgrid-example.com/7thcrownworks3d/

Additional images can be provided.

I just didn't see where to set the date.

Target Market(s)

Fundlaunch, 3d printing tabletop gamers

Font styles to use
Sans Serif

Requirements
Must have
• - Header design (I use images rather than fonts for titles) template in psd format that can have its text and colour changed easily by a third party, with a suitable sci-fi font. 680 px wide, height whatever looks good, but should be horizontal text.
- A sci-fi frame design template for presenting 3D renders (with alpha channels; 680 px wide, variable height) of miniatures, add-ons, stretch goals, framing photographic images, and presenting information, such as a chart of various campaign pledges
- Small Icons (less than 100×100, probably closer to 50×50) for locked and unlocked to be used in the frame above to show whether a stretch goal has been reached or is still being worked towards
Nice to have
• You could integrate the silhouette of the ship or features of the ship into the design, or follow a logical theme, such as a hangar bay, or having the graphics have RCS thrusters or something thematic like that.

The use of colour in the font/graphic to lift monotone renders is ideal
Should not have
• Should not be too gaudy or cluttered

```html
<!DOCTYPE html>
<html lang="en">
<head>
<meta charset="utf-8">
<title>Voidcraft Q – Campaign Graphic Kit</title>
<link rel="stylesheet" href="https://fonts.googleapis.com/css2?family=Chakra+Petch:ital,wght@0,400;0,600;0,700;1,400&family=Geo&display=swap">
<style>
  :root {
    --bg: #1b1c23;
    --bg-edge: #141a33;
    --panel: #03040b;
    --panel-2: #05060f;
    --blue: #0a3dff;
    --bone: #dfe3d6;
    --white: #f4f5f2;
    --grey-slant: #3a3a3c;
    --grey-strip: #1d1d1f;
    --red: #7d0202;
    --red-line: #c10707;
    --green: #129a12;
    --green-line: #0fa10f;
    --label: #f1f1f1;
  }
  * { box-sizing: border-box; margin: 0; padding: 0; }
  html, body { width: 1200px; height: 675px; overflow: hidden; background: var(--bg); }
  .sheet {
    position: relative; width: 1200px; height: 675px; overflow: hidden;
    background:
      radial-gradient(ellipse at 0% 10%, rgba(30,50,130,.45), transparent 40%),
      radial-gradient(ellipse at 100% 100%, rgba(30,50,130,.35), transparent 40%),
      radial-gradient(ellipse at 5% 60%, rgba(30,50,120,.25), transparent 35%),
      var(--bg);
    font-family: "Chakra Petch", sans-serif; color: var(--label);
  }
  .label {
    position: absolute; font-family: "Geo", sans-serif; color: var(--label);
    text-align: center; letter-spacing: 2px; line-height: 1; transform: translateX(-50%);
    white-space: nowrap;
  }
  .label--lg { font-size: 20px; }
  .label--sm { font-size: 14px; line-height: 18px; letter-spacing: 1.5px; }

  .splash {
    position: absolute; left: 72px; top: 28px; width: 630px; height: 354px;
    background: radial-gradient(ellipse at 60% 40%, #070a1c, var(--panel) 70%);
    overflow: hidden;
  }
  .render {
    position: absolute;
    background: radial-gradient(ellipse at 50% 50%, #5a5258 0%, #2a2629 45%, transparent 72%);
  }
  .splash .render { left: 54px; top: 12px; width: 520px; height: 227px; }
  .splash svg { position: absolute; left: 0; top: 0; }
  .splash-title {
    position: absolute; left: 148px; width: 362px; top: 262px; height: 68px;
    font-family: "Geo", sans-serif; font-size: 62px; line-height: 68px;
    letter-spacing: 6px; text-align: center; color: var(--white); white-space: nowrap;
  }

  .backdrop {
    position: absolute; left: 767px; top: 29px; width: 355px; height: 355px;
    background:
      repeating-linear-gradient(90deg, rgba(60,80,160,.07) 0 1px, transparent 1px 44px),
      repeating-linear-gradient(0deg, rgba(60,80,160,.07) 0 1px, transparent 1px 44px),
      var(--panel-2);
  }

  .goal-card {
    position: absolute; top: 424px; width: 223px; height: 224px;
    background: #000;
  }
  .goal-card--locked { left: 73px; }
  .goal-card--unlocked { left: 352px; background: #01020a; }
  .goal-card__head { position: absolute; left: 0; top: 0; width: 223px; height: 27px; background: var(--grey-strip); }
  .goal-card--unlocked .goal-card__head { background: #07080f; }
  .goal-card__head svg { position: absolute; left: 0; top: 0; }
  .goal-card__name, .goal-card__price {
    position: absolute; top: 0; line-height: 27px; font-size: 13.5px; color: var(--white); white-space: nowrap;
  }
  .goal-card__name { left: 30px; font-style: italic; }
  .goal-card__price { left: 139px; }
  .goal-card .render { left: 9px; top: 56px; width: 206px; height: 96px; }
  .goal-card--locked .render { background: radial-gradient(ellipse at 50% 50%, #6a6a6a 0%, #333 45%, transparent 72%); }
  .goal-card--unlocked .render { background: radial-gradient(ellipse at 50% 50%, #7a7a7a 0%, #3a3a3a 45%, transparent 72%); }
  .goal-card__status { position: absolute; left: 0; top: 150px; }
  .status-text { font-family: "Chakra Petch", sans-serif; font-weight: 700; font-size: 38px; letter-spacing: -1px; }

  .frame-header { position: absolute; left: 718px; top: 448px; }

  .fonts-note {
    position: absolute; left: 905px; top: 537px; transform: translateX(-50%);
    font-style: italic; font-size: 15px; white-space: nowrap;
  }
  .font-sample { position: absolute; left: 905px; transform: translateX(-50%); white-space: nowrap; line-height: 1; }
  .font-sample--geo { top: 568px; font-family: "Geo", sans-serif; font-size: 36px; letter-spacing: 2px; }
  .font-sample--petch { top: 610px; font-family: "Chakra Petch", sans-serif; font-size: 30px; }
</style>
</head>
<body>
<main class="sheet">

  <p class="label label--lg" style="left:384px; top:8px;">SPLASH IMAGE</p>
  <section class="splash">
    <div class="render" role="img" aria-label="3D render of the Voidcraft Q spaceship miniature"></div>
    <svg width="630" height="354" viewBox="0 0 630 354" aria-hidden="true">
      <polygon points="82,264 121,264 92,329 52,329" fill="var(--blue)"/>
      <polygon points="129,264 147,264 116,329 100,329" fill="var(--bone)"/>
      <polygon points="532,264 559,264 528,329 502,329" fill="var(--blue)"/>
    </svg>
    <h1 class="splash-title">VOIDCRAFT Q</h1>
  </section>

  <p class="label label--lg" style="left:942px; top:9px;">GENERAL USE BACKGROUND</p>
  <section class="backdrop" aria-label="General use background"></section>

  <p class="label label--sm" style="left:180px; top:388px;">STRETCH GOAL LOCKED<br>[MUTED COLORS]</p>
  <article class="goal-card goal-card--locked">
    <div class="goal-card__head">
      <svg width="223" height="27" viewBox="0 0 223 27" aria-hidden="true">
        <polygon points="0,0 12,0 1,27 0,27" fill="var(--grey-slant)"/>
        <polygon points="17,0 31,0 21,27 7,27" fill="var(--bone)"/>
        <polygon points="114,0 133,0 124,27 105,27" fill="var(--grey-slant)"/>
        <polygon points="217,0 223,0 223,27 210,27" fill="var(--grey-slant)"/>
      </svg>
      <span class="goal-card__name">ITEM NAME</span>
      <span class="goal-card__price">100k SEK</span>
    </div>
    <div class="render" role="img" aria-label="Muted render of the stretch goal item"></div>
    <svg class="goal-card__status" width="223" height="74" viewBox="0 0 223 74" aria-hidden="true">
      <polygon points="81,5 164,5 143,59 60,59" fill="var(--red)"/>
      <text class="status-text" x="111" y="43" text-anchor="middle" fill="#140000" stroke="var(--red-line)" stroke-width="1.2">LOCKED</text>
    </svg>
  </article>

  <p class="label label--sm" style="left:464px; top:388px;">STRETCH GOAL UNLOCKED<br>[FULL COLORS]</p>
  <article class="goal-card goal-card--unlocked">
    <div class="goal-card__head">
      <svg width="223" height="27" viewBox="0 0 223 27" aria-hidden="true">
        <polygon points="0,0 12,0 1,27 0,27" fill="var(--blue)"/>
        <polygon points="17,0 31,0 21,27 7,27" fill="var(--bone)"/>
        <polygon points="114,0 133,0 124,27 105,27" fill="var(--blue)"/>
        <polygon points="217,0 223,0 223,27 210,27" fill="var(--blue)"/>
      </svg>
      <span class="goal-card__name">ITEM NAME</span>
      <span class="goal-card__price">100k SEK</span>
    </div>
    <div class="render" role="img" aria-label="Full colour render of the stretch goal item"></div>
    <svg class="goal-card__status" width="223" height="74" viewBox="0 0 223 74" aria-hidden="true">
      <polygon points="0,6 34,6 18,59 0,59" fill="var(--green)"/>
      <polygon points="214,6 223,6 223,59 191,59" fill="var(--green)"/>
      <text class="status-text" x="112" y="43" text-anchor="middle" textLength="198" lengthAdjust="spacingAndGlyphs" fill="#001400" stroke="var(--green-line)" stroke-width="1.2">UNLOCKED!</text>
    </svg>
  </article>

  <p class="label label--lg" style="left:921px; top:421px;">FRAME HEADER / TEXT FRAME</p>
  <svg class="frame-header" width="380" height="74" viewBox="0 0 380 74" aria-label="Frame header">
    <polygon points="100,0 350,0 314,74 66,74" fill="#06050b"/>
    <polygon points="37,0 81,0 46,74 0,74" fill="var(--blue)"/>
    <polygon points="93,0 111,0 74,74 56,74" fill="var(--bone)"/>
    <polygon points="349,0 380,0 343,74 311,74" fill="var(--blue)"/>
  </svg>

  <p class="fonts-note">FONTS USED (available for free through Typeshelf Library):</p>
  <p class="font-sample font-sample--geo">GEO</p>
  <p class="font-sample font-sample--petch">Chakra Petch</p>

</main>
</body>
</html>
```